New business card for civil engineering company - "Keystone Audit"

We need a business card designed for our new structural engineering company.

The company name is "Keystone Audit" logo files attached.

We would like the following:
* Two-sided card
* Simple design

Information to be placed on the card:
Name - Marcus Dellow
Job Title - Director / Structural Engineer
Credentials - BEng(Hons), CPEng, CMengNZ, IntPE(NZ)
Email - marcus.dellow@keystoneaudit.co.nz
mobile - 0219364058
website - www.keystoneaudit.co.nz

```html
<!DOCTYPE html>
<html lang="en">
<head>
<meta charset="utf-8">
<title>Keystone Audit – Business Card</title>
<link href="https://fonts.googleapis.com/css2?family=Montserrat:wght@300;400;600;700&display=swap" rel="stylesheet">
<style>
  :root {
    --backdrop: #5d6163;
    --card-dark: #221e1f;
    --card-light: #ffffff;
    --navy: #1c3d6b;
    --ink-blue: #2b5c97;
    --brand-blue: #5b9be0;
    --divider: #2b5c97;
  }
  * { margin: 0; padding: 0; box-sizing: border-box; }
  html, body {
    width: 1200px; height: 1200px; overflow: hidden;
    background: var(--backdrop);
    font-family: "Montserrat", sans-serif;
  }
  .canvas {
    position: relative; width: 1200px; height: 1200px;
  }
  .card {
    position: absolute; left: 180px; width: 840px; height: 480px;
    border-radius: 30px;
    box-shadow: 0 10px 30px rgba(0,0,0,0.35);
  }
  .card--front { top: 90px; background: var(--card-dark); }
  .card--back  { top: 630px; background: var(--card-light); }

  .brand-lockup {
    position: absolute; left: 50%; top: 50%;
    transform: translate(-50%, -50%);
    display: flex; align-items: center; gap: 18px;
    font-weight: 600; font-size: 40px; letter-spacing: 3px;
    text-transform: uppercase; white-space: nowrap;
  }
  .brand-lockup__square { width: 34px; height: 34px; background: var(--brand-blue); }
  .card--front .brand-lockup { color: #ffffff; }

  .divider {
    position: absolute; left: 560px; top: 70px;
    width: 2px; height: 260px; background: var(--divider);
  }
  .card--back .brand-lockup {
    left: 700px; top: 200px; flex-direction: column; gap: 14px;
    font-size: 26px; color: var(--brand-blue); letter-spacing: 2px;
  }
  .card--back .brand-lockup__square { width: 60px; height: 60px; }

  .contact {
    position: absolute; left: 110px; top: 190px;
    color: var(--ink-blue); font-size: 22px; font-weight: 400; line-height: 1.3;
  }
  .contact__name { font-size: 32px; color: var(--navy); font-weight: 300; margin-bottom: 6px; }
  .contact__name strong { font-weight: 700; }
  .contact__credentials { margin-top: 10px; }
  .contact__details { margin-top: 26px; }
</style>
</head>
<body>
<main class="canvas">
  <section class="card card--front" aria-label="Card front">
    <div class="brand-lockup">
      <span class="brand-lockup__square"></span>
      <span class="brand-lockup__name">Keystone Audit</span>
    </div>
  </section>

  <section class="card card--back" aria-label="Card back">
    <div class="contact">
      <p class="contact__name"><strong>Marcus</strong> Dellow</p>
      <p class="contact__title">Director / Structural Engineer</p>
      <p class="contact__credentials">BEng(Hons), CPEng,<br>CMengNZ, IntPE(NZ)</p>
      <div class="contact__details">
        <p>0219364058</p>
        <p>marcus.dellow@keystoneaudit.co.nz</p>
        <p>www.keystoneaudit.co.nz</p>
      </div>
    </div>
    <div class="divider"></div>
    <div class="brand-lockup">
      <span class="brand-lockup__square"></span>
      <span class="brand-lockup__name">Keystone Audit</span>
    </div>
  </section>
</main>
</body>
</html>
```